Business Card Design

I do estate sales and would like business card to reflect look and feel of attached logo. I also have copy of logo in .eps and .tif if you need that instead of .jpeg.
Updates

sorry for the delay in reviewing these designs. I will pick one by tomorrow. Here are the absolutes: *must have tagline (we find good homes for your treasures *must use blue and green *must be horizontal *nothing too fancy please submit your best and final. Thanks so much!

Industry/Entity Type

Business

Contact Information for Business Card

Mira Tolland

TAGS by MIRA
We find good homes for your treasures.

Specializing in one to three-day sales
o (no sale too big or too small)
• Home and garage organizing
• Home Clean-out

Call Mira Tolland at 202-555-0147
to schedule.

```html
<!DOCTYPE html>
<html lang="en">
<head>
<meta charset="utf-8">
<title>TAGS by MIRA — Business Card</title>
<link rel="stylesheet" href="https://fonts.googleapis.com/css2?family=Archivo+Black&family=Roboto:ital,wght@0,300;0,400;1,300;1,400;1,700&display=swap">
<style>
  :root {
    --card-bg: #ffffff;
    --leaf-green: #6f8a3e;
    --teal: #2a86a4;
    --ink-navy: #0f3f52;
    --body-ink: #1f2a30;
    --ring-sage: #b7bc9f;
    --ring-sky: #9cc9d5;
  }
  html, body {
    margin: 0;
    padding: 0;
    width: 1200px;
    height: 702px;
    overflow: hidden;
    background: var(--card-bg);
  }
  .card {
    position: relative;
    width: 1200px;
    height: 702px;
    background: var(--card-bg);
    overflow: hidden;
    font-family: "Roboto", Arial, sans-serif;
    color: var(--body-ink);
  }
  .card__rings {
    position: absolute;
    inset: 0;
    width: 1200px;
    height: 702px;
  }
  .brand {
    position: absolute;
    left: 93px;
    top: 130px;
    width: 370px;
    height: 300px;
    display: flex;
    align-items: center;
  }
  .brand__name {
    margin: 0;
    font-family: "Roboto", Arial, sans-serif;
    font-size: 56px;
    font-weight: 400;
    font-style: normal;
    color: var(--leaf-green);
    line-height: 1;
    white-space: nowrap;
  }
  .tagline {
    position: absolute;
    left: 93px;
    top: 444px;
    margin: 0;
    font-size: 20px;
    font-style: italic;
    font-weight: 400;
    color: var(--teal);
  }
  .divider {
    position: absolute;
    left: 487px;
    top: 130px;
    width: 3px;
    height: 337px;
    background: var(--teal);
  }
  .contact {
    position: absolute;
    left: 520px;
    top: 230px;
  }
  .contact__name {
    margin: 0;
    font-family: "Archivo Black", "Arial Black", sans-serif;
    font-size: 52px;
    font-weight: 400;
    color: var(--ink-navy);
    letter-spacing: 0.5px;
    line-height: 1;
  }
  .contact__phone {
    margin: 22px 0 0 3px;
    font-size: 34px;
    font-weight: 300;
    color: var(--ink-navy);
    line-height: 1;
  }
  .contact__note {
    margin: 10px 0 0 3px;
    font-size: 21px;
    font-style: italic;
    font-weight: 300;
    color: var(--body-ink);
  }
  .services {
    position: absolute;
    left: 93px;
    top: 504px;
  }
  .services__title {
    margin: 0;
    font-size: 23px;
    font-style: italic;
    font-weight: 700;
    color: var(--ink-navy);
  }
  .services__list {
    margin: 10px 0 0;
    padding: 0;
    list-style: none;
    display: flex;
    font-size: 25px;
    font-weight: 300;
  }
  .services__list li + li::before {
    content: "•";
    margin: 0 8px;
  }
</style>
</head>
<body>
  <div class="card">
    <svg class="card__rings" viewBox="0 0 1200 702" aria-hidden="true">
      <circle cx="477" cy="122" r="635" fill="none" stroke="var(--ring-sage)" stroke-width="4"/>
      <circle cx="1209" cy="590" r="392" fill="none" stroke="var(--ring-sky)" stroke-width="11"/>
    </svg>

    <div class="brand">
      <p class="brand__name">TAGS by MIRA</p>
    </div>
    <p class="tagline">We find good homes for your treasures</p>

    <div class="divider"></div>

    <div class="contact">
      <h1 class="contact__name">Mira Tolland</h1>
      <p class="contact__phone">202.555.0147</p>
      <p class="contact__note">call to schedule an appointment</p>
    </div>

    <div class="services">
      <h2 class="services__title">Specialities</h2>
      <ul class="services__list">
        <li>1-3 day sales</li>
        <li>home and garage organizing</li>
        <li>home clean-out</li>
      </ul>
    </div>
  </div>
</body>
</html>
```